Need a book cover design for a Lumora Book on Herbal Remedies

I need a book cover for my new ebook, here are the details:
Title: Meadow Cures
Sub-Heading: Buried Ancient Garden Tonics
Reclaiming the Wisdom of Roots for Everyday Wellness and Strength
Author: Nora Belcourt

```html
<!DOCTYPE html>
<html lang="en">
<head>
<meta charset="utf-8">
<title>Meadow Cures — Nora Belcourt</title>
<link rel="stylesheet" href="https://fonts.googleapis.com/css2?family=League+Spartan:wght@300;400;700&family=Josefin+Sans:wght@700&family=Poppins:wght@400&display=swap">
<style>
  :root {
    --backdrop: #b0b0b0;
    --paper: #f3f3f2;
    --paper-shade: #e7e7e5;
    --leaf-green: #6b7019;
    --bark-brown: #85501a;
    --band-dark: #2e1a0b;
    --band-light: #5a3516;
    --ink: #2b2b2b;
    --bowl-rim: #9c6435;
    --bowl-inner: #b98a4e;
    --herb-green: #a8b57a;
  }
  * { margin: 0; padding: 0; box-sizing: border-box; }
  html, body { width: 1200px; height: 1033px; overflow: hidden; }
  body { background: var(--backdrop); position: relative; }

  .cover {
    position: absolute;
    left: 329px; top: 86px;
    width: 541px; height: 866px;
    overflow: hidden;
    background: linear-gradient(180deg, #f8f8f7 0%, var(--paper) 45%, var(--paper-shade) 100%);
    box-shadow: 6px 8px 14px rgba(0,0,0,0.18);
  }

  .title { position: absolute; left: 55px; top: 58px; line-height: 1; width: 445px; }
  .title-main {
    display: block;
    font-family: "League Spartan", sans-serif;
    font-weight: 700;
    font-size: 104px;
    letter-spacing: -1px;
    color: var(--leaf-green);
    height: 94px;
    white-space: nowrap;
  }
  .title-second {
    display: block;
    font-family: "League Spartan", sans-serif;
    font-weight: 400;
    font-size: 112px;
    letter-spacing: 8px;
    color: var(--bark-brown);
    white-space: nowrap;
  }

  .subtitle-band {
    position: absolute;
    left: 55px; top: 256px;
    width: 443px; height: 31px;
    border-radius: 4px;
    background: linear-gradient(90deg, var(--band-dark), var(--band-light));
    box-shadow: 0 3px 5px rgba(0,0,0,0.25);
    color: #fff;
    font-family: "Josefin Sans", sans-serif;
    font-weight: 700;
    font-size: 16.5px;
    letter-spacing: 3px;
    text-align: center;
    line-height: 34px;
    white-space: nowrap;
  }

  .herb-bowl {
    position: absolute;
    left: 205px; top: 318px;
    width: 488px; height: 488px;
  }

  .tagline {
    position: absolute;
    left: 56px; top: 380px;
    width: 165px;
    font-family: "Poppins", sans-serif;
    font-size: 18.5px;
    line-height: 26.6px;
    color: var(--ink);
  }
  .tagline-rule {
    position: absolute;
    left: 58px; top: 552px;
    width: 39px; height: 3px;
    background: var(--bark-brown);
  }

  .author { position: absolute; left: 55px; top: 710px; line-height: 1; }
  .author-first {
    display: block;
    font-family: "League Spartan", sans-serif;
    font-weight: 700;
    font-size: 48px;
    color: var(--leaf-green);
  }
  .author-last {
    display: block;
    font-family: "League Spartan", sans-serif;
    font-weight: 400;
    font-size: 46px;
    color: var(--bark-brown);
    margin-top: 0;
  }
</style>
</head>
<body>
  <div class="cover">
    <h1 class="title">
      <span class="title-main">MEADOW</span>
      <span class="title-second">CURES</span>
    </h1>

    <p class="subtitle-band">BURIED ANCIENT GARDEN TONICS</p>

    <svg class="herb-bowl" viewBox="0 0 488 488" role="img" aria-label="Photo of a wooden bowl filled with dried linden leaves and yellow blossoms">
      <defs>
        <radialGradient id="bowlFill" cx="50%" cy="50%" r="50%">
          <stop offset="0%" stop-color="var(--herb-green)"/>
          <stop offset="62%" stop-color="#b7ad5a"/>
          <stop offset="84%" stop-color="var(--bowl-inner)"/>
          <stop offset="100%" stop-color="var(--bowl-rim)"/>
        </radialGradient>
      </defs>
      <circle cx="250" cy="246" r="242" fill="rgba(0,0,0,0.16)"/>
      <circle cx="244" cy="244" r="242" fill="url(#bowlFill)"/>
    </svg>

    <p class="tagline">Reclaiming the Wisdom of Roots for Everyday Wellness and Strength</p>
    <div class="tagline-rule"></div>

    <p class="author">
      <span class="author-first">NORA</span>
      <span class="author-last">BELCOURT</span>
    </p>
  </div>
</body>
</html>
```